We would like to incorporate our logo into letterhead design and envelopes. We are looking for something that is moderately conservative but not old law firm style. Both the envelopes and the letterhead must have both firm addresses. We would like to incorporate the color of the logo, but only a small amount of color - perhaps on one of the borders. The addresses for the firm locations are listed below. Given that it is a law firm, it needs to somewhat conservative, but not the old school, small black font on cream colored paper design.

The firm addresses are:

27815 N. Harlow Pemberton Pkwy.
Ste 4200
Scottsdale, AZ 85391

6100 W. Cedar Avenue
Ste 700
Burbank, CA 91623

Industry/Entity Type

Legal

Colors

Designer to choose colors to be used in the design.

Requirements
Must have
• Both addresses:
• 27815 N. Harlow Pemberton Pkwy.
• Ste 4200
• Scottsdale, AZ 85391
• 6100 W. Cedar Avenue
• Ste 700
• Burbank, CA 91623
Nice to have
• Small amount of color on border(s) that matches the logo but not too much color

```html
<!DOCTYPE html>
<html lang="en">
<head>
<meta charset="utf-8">
<title>Veyland Law — Letterhead and Envelope</title>
<link href="https://fonts.googleapis.com/css2?family=Cormorant+Garamond:wght@500&family=Lato:ital,wght@0,300;0,400;1,300&display=swap" rel="stylesheet">
<style>
  :root {
    --backdrop: #e8e9eb;
    --paper: #fdf8ea;
    --flap: #f6f2e6;
    --navy: #2a2566;
    --ink: #4a4a4a;
    --watermark: rgba(150, 150, 150, 0.22);
    --vertical-mark: #9a9a9a;
    --signature-tone: #d9d3c4;
  }
  * { margin: 0; padding: 0; box-sizing: border-box; }
  html, body {
    width: 1200px; height: 896px; overflow: hidden;
    background: var(--backdrop);
  }
  .stationery { position: relative; width: 1200px; height: 896px; }

  /* Letterhead */
  .letterhead {
    position: absolute; left: 130px; top: 134px;
    width: 461px; height: 600px;
    background: var(--paper);
    overflow: hidden;
  }
  .letterhead__band {
    position: absolute; left: 0; top: 48px; width: 461px; height: 51px;
  }
  .letterhead__band-stub {
    position: absolute; left: 0; top: 0; width: 36px; height: 100%;
    background: var(--navy);
  }
  .letterhead__name {
    position: absolute; left: 36px; top: 0; width: 121px; height: 100%;
    display: flex; align-items: center; justify-content: center;
    font-family: "Cormorant Garamond", serif; font-weight: 500;
    font-size: 15px; letter-spacing: 0.3px; color: var(--navy);
    white-space: nowrap;
  }
  .letterhead__band-main {
    position: absolute; left: 157px; top: 0; right: 0; height: 100%;
    background: var(--navy);
    display: flex; gap: 30px; align-items: center; padding-left: 26px;
  }
  .address {
    font-family: "Lato", sans-serif; font-weight: 300;
    font-size: 9.4px; line-height: 12.5px; color: #ffffff;
    white-space: nowrap;
  }
  .letterhead__date {
    position: absolute; left: 46px; top: 150px;
    font-family: "Lato", sans-serif; font-weight: 300;
    font-size: 9.5px; letter-spacing: 0.3px; color: var(--ink);
  }
  .letterhead__watermark {
    position: absolute; left: 232px; top: 295px;
    transform: translate(-50%, -50%) rotate(-45deg);
    font-family: "Cormorant Garamond", serif; font-weight: 500;
    font-size: 46px; letter-spacing: 1px; color: var(--watermark);
    white-space: nowrap;
  }
  .letterhead__closing {
    position: absolute; left: 54px; top: 456px;
    font-family: "Lato", sans-serif; font-style: italic; font-weight: 300;
    font-size: 13px; color: var(--ink);
  }
  .letterhead__signature {
    position: absolute; left: 46px; top: 481px;
    width: 176px; height: 52px;
    background: var(--signature-tone); opacity: 0.5;
  }
  .letterhead__footer {
    position: absolute; left: 32px; right: 0; top: 559px;
    display: flex; align-items: center; gap: 8px;
  }
  .letterhead__web {
    font-family: "Lato", sans-serif; font-weight: 400;
    font-size: 9.5px; color: var(--ink); white-space: nowrap;
  }
  .letterhead__rule { flex: 1; height: 5px; background: var(--navy); }

  /* Envelope */
  .envelope {
    position: absolute; left: 646px; top: 115px;
    width: 487px; height: 629px;
    background: var(--paper);
    overflow: hidden;
  }
  .envelope__flap { position: absolute; left: 0; top: 0; width: 487px; height: 72px; }
  .envelope__name {
    position: absolute; left: 244px; top: 20px;
    font-family: "Cormorant Garamond", serif; font-weight: 500;
    font-size: 28px; letter-spacing: 0.5px; color: var(--navy);
    white-space: nowrap;
  }
  .envelope__vertical-name {
    position: absolute; left: 75px; top: 347px;
    transform: translate(-50%, -50%) rotate(-90deg);
    font-family: "Cormorant Garamond", serif; font-weight: 500;
    font-size: 46px; letter-spacing: 1px; color: var(--vertical-mark);
    white-space: nowrap;
  }
  .envelope__addresses {
    position: absolute; right: 36px; bottom: 34px;
    display: flex; gap: 30px;
    padding-top: 10px;
    border-top: 2px solid var(--navy);
  }
  .envelope__addresses .address { color: var(--ink); }
</style>
</head>
<body>
<main class="stationery">

  <section class="letterhead" aria-label="Letterhead">
    <div class="letterhead__band">
      <div class="letterhead__band-stub"></div>
      <div class="letterhead__name">VEYLAND LAW</div>
      <div class="letterhead__band-main">
        <p class="address">6100 W. Cedar Avenue<br>Ste 700<br>Burbank, CA 91623</p>
        <p class="address">27815 N. Harlow<br>Pemberton Pkwy. Ste 4200<br>Scottsdale, AZ 85391</p>
      </div>
    </div>
    <p class="letterhead__date">DATE : 20 NOV 2019</p>
    <p class="letterhead__watermark" aria-hidden="true">VEYLAND LAW</p>
    <p class="letterhead__closing">Yours faithfully</p>
    <div class="letterhead__signature" role="img" aria-label="Handwritten signature"></div>
    <div class="letterhead__footer">
      <span class="letterhead__web">www.veylandlaw.com</span>
      <span class="letterhead__rule"></span>
    </div>
  </section>

  <section class="envelope" aria-label="Envelope">
    <svg class="envelope__flap" viewBox="0 0 487 72" aria-hidden="true">
      <path d="M0 0 H487 V42 Q487 58 470 62 Q243 78 17 62 Q0 58 0 42 Z" fill="var(--flap)"/>
    </svg>
    <p class="envelope__name">VEYLAND LAW</p>
    <p class="envelope__vertical-name">VEYLAND LAW</p>
    <div class="envelope__addresses">
      <p class="address">6100 W. Cedar Avenue<br>Ste 700<br>Burbank, CA 91623</p>
      <p class="address">27815 N. Harlow<br>Pemberton Pkwy. Ste 4200<br>Scottsdale, AZ 85391</p>
    </div>
  </section>

</main>
</body>
</html>
```